Carpentry company Needs a business card design

We need a design for a Carpentry / building company, business card. Please think of designs out of the ordinary and try to make it eye catching. Our existing logo will need to be incorporated in the design. However feel free to change the colours of the logo to suit your design. I would like to see some designs with green /black and orange incorporated into it.These are not the only colours accepted and all designs that appeal will be accepted.

Please contact me should you have any questions
Thanks Martin

Target Market(s)

General Public seeking carpentry work

Industry/Entity Type

Business

Contact Information for Business Card

- Current company logo ( colours can be changed)
-Phone number ,
- info@brelvanbuild.com.au
- brelvanbuild.com.au
-the facebook symbol

Font styles to use
Other font styles liked:
• You choose

Requirements
Must have
• Services we provide
• - Renovations
• -Deckings & Pergolas
• -Kitchens
• - Bathrooms
• - Intricate details
Nice to have
• an awesome design
Should not have
• Tools on the business card

```html
<!DOCTYPE html>
<html lang="en">
<head>
<meta charset="utf-8">
<title>Brelvan Build – Business Card</title>
<link href="https://fonts.googleapis.com/css2?family=Roboto:wght@400;500;700&display=swap" rel="stylesheet">
<style>
  :root {
    --backdrop: #3b3431;
    --card-black: #1c1c1e;
    --card-black-edge: #2a2a2c;
    --gloss-grey: #3d3d40;
    --white: #ffffff;
    --muted: #c9c9c9;
    --green: #7dc242;
    --orange: #f47b20;
    --ink: #1a1a1a;
  }
  * { margin: 0; padding: 0; box-sizing: border-box; }
  html, body {
    width: 1200px; height: 716px; overflow: hidden;
    background: var(--backdrop);
    font-family: "Roboto", Arial, sans-serif;
  }
  .canvas { position: relative; width: 1200px; height: 716px; }

  .card {
    position: absolute; top: 193px;
    width: 540px; height: 330px;
    background: linear-gradient(135deg, var(--card-black-edge), var(--card-black));
    border-radius: 4px; overflow: hidden;
    box-shadow: 0 10px 24px rgba(0,0,0,.35);
  }
  .card--back { left: 45px; }
  .card--front { left: 615px; }

  /* Brand lockup */
  .brand { display: flex; align-items: center; gap: 10px; }
  .brand__square { width: 18px; height: 18px; flex: none; }
  .brand__name { font-weight: 700; letter-spacing: 2px; line-height: 1; white-space: nowrap; }

  .card--back .brand {
    position: absolute; left: 0; right: 0; top: 100px; justify-content: center;
  }
  .card--back .brand__square { background: var(--gloss-grey); width: 26px; height: 26px; }
  .card--back .brand__name { color: var(--gloss-grey); font-size: 44px; }

  .tagline {
    position: absolute; left: 0; right: 0; top: 196px;
    display: flex; align-items: center; justify-content: center; gap: 18px;
    color: var(--green); font-size: 15px; letter-spacing: 1px;
  }
  .tagline__rule { width: 44px; height: 3px; background: var(--orange); }

  /* Front side */
  .person { position: absolute; left: 58px; top: 36px; }
  .person__name { color: var(--white); font-size: 18px; font-weight: 700; }
  .person__role { color: var(--muted); font-size: 11px; margin-top: 3px; }

  .contacts { position: absolute; left: 58px; top: 100px; list-style: none; }
  .contacts li {
    display: flex; align-items: center; gap: 8px;
    color: var(--white); font-size: 12px; height: 17px;
  }
  .contacts svg { width: 10px; height: 10px; flex: none; }

  .card--front .brand { position: absolute; right: 36px; top: 116px; }
  .card--front .brand__square { background: var(--green); }
  .card--front .brand__name { color: var(--white); font-size: 26px; }

  .wave { position: absolute; left: 0; top: 0; width: 540px; height: 330px; }

  .services {
    position: absolute; right: 28px; bottom: 14px;
    list-style: none; text-align: right;
    color: var(--ink); font-size: 14px; font-weight: 500; line-height: 17px;
  }
</style>
</head>
<body>
<main class="canvas">

  <section class="card card--back" aria-label="Card back">
    <div class="brand">
      <span class="brand__square"></span>
      <span class="brand__name">BRELVAN BUILD</span>
    </div>
    <p class="tagline">
      <span class="tagline__rule"></span>
      <span>Carpentry at its Best</span>
      <span class="tagline__rule"></span>
    </p>
  </section>

  <section class="card card--front" aria-label="Card front">
    <svg class="wave" viewBox="0 0 540 330" aria-hidden="true">
      <path fill="var(--green)" d="M0,205 C140,210 220,268 350,258 C450,250 500,218 540,212 L540,330 L0,330 Z"/>
      <path fill="none" stroke="var(--orange)" stroke-width="9" d="M0,186 C150,190 230,250 360,240 C450,232 500,202 540,196"/>
      <path fill="none" stroke="var(--orange)" stroke-width="3" d="M0,196 C140,200 225,258 345,250"/>
    </svg>

    <div class="person">
      <p class="person__name">Your Good Name</p>
      <p class="person__role">Managing Director</p>
    </div>

    <ul class="contacts">
      <li>
        <svg viewBox="0 0 10 10"><rect width="10" height="10" rx="2" fill="var(--green)"/><path d="M3,2 L4.3,3.5 L3.6,4.3 Q4.5,6 5.8,6.5 L6.6,5.8 L8,7.2 L7,8.2 Q3.5,7.5 2,3 Z" fill="var(--card-black)"/></svg>
        0400 555 017
      </li>
      <li>
        <svg viewBox="0 0 10 10"><rect width="10" height="10" rx="2" fill="var(--green)"/><rect x="2" y="3" width="6" height="4.2" fill="var(--card-black)"/><path d="M2,3 L5,5.4 L8,3" stroke="var(--green)" stroke-width=".8" fill="none"/></svg>
        info@brelvanbuild.com.au
      </li>
      <li>
        <svg viewBox="0 0 10 10"><rect width="10" height="10" rx="2" fill="var(--green)"/><circle cx="5" cy="5" r="2.8" fill="none" stroke="var(--card-black)" stroke-width="1"/><path d="M2.2,5 H7.8 M5,2.2 V7.8" stroke="var(--card-black)" stroke-width=".8"/></svg>
        www.brelvanbuild.com.au
      </li>
      <li>
        <svg viewBox="0 0 10 10"><rect width="10" height="10" rx="2" fill="var(--green)"/></svg>
        /Brelvan-Build
      </li>
    </ul>

    <div class="brand">
      <span class="brand__square"></span>
      <span class="brand__name">BRELVAN BUILD</span>
    </div>

    <ul class="services">
      <li>Renovations «</li>
      <li>Deckings &amp; Pergolas «</li>
      <li>Kitchens « Bathrooms «</li>
      <li>New Home « Extensions «</li>
    </ul>
  </section>

</main>
</body>
</html>
```